Stridewell Clinic (Podiatry and Physiotherapy) Clinical Brochure

You are producing a brochure that will sit in clinical/medical waiting rooms for our business Stridewell Clinic. A clinic that providers podiatry and physiotherapy services.

As you can see on our website www.stridewellclinic.example.nz we provide 6 different brands/services:
- Brightmoor Solutions
- Kestrelbay Solutions
- Varden Solutions
- Tolverstone Rehabilitation
- Ashgrove Solutions
- Merriwether Solutions

People will generally have found us through an ad e.g. search fungal nail treatment and end up straight on www.brightmoorsolutions.example.nz and therefore, each of the brands should be seen as being separate entities although part of the bigger brand Stridewell Clinic.

We are looking at a brochure (open to bi-fold, tri-fold etc.) that highlights all of our brands as well as the services that each of our brands provide which can be found on each of the websites listed above. We want this to be professional and informative yet simple and easy to read - this interpretation can be somewhat left up to you. This brochure will sit in waiting rooms/clinical environments.

I have attached our brand strategy so that you can understand our fonts and colours. I have also attached our logos for reference.

```html
<!DOCTYPE html>
<html lang="en">
<head>
<meta charset="utf-8">
<title>Stridewell Clinic – Brochure Cover</title>
<link href="https://fonts.googleapis.com/css2?family=Arimo:wght@400;700&display=swap" rel="stylesheet">
<style>
  :root {
    --brand-blue: #2c6db4;
    --ink: #1f1f1f;
    --ink-soft: #3f3f3f;
    --ink-muted: #6a6a6a;
    --rule: #d6e2f0;
    --paper: #ffffff;
    --xray-deep: #0a5fd0;
    --xray-mid: #3f93ea;
    --xray-light: #e9f4ff;
    --skin-light: #f6dccb;
    --skin-mid: #e8bc9f;
  }
  html, body {
    margin: 0;
    padding: 0;
    overflow: hidden;
    background: var(--paper);
  }
  .brochure {
    position: relative;
    width: 1200px;
    height: 848px;
    overflow: hidden;
    background: var(--paper);
    font-family: "Arimo", Arial, sans-serif;
    color: var(--ink);
  }

  /* Left panel: anatomical foot artwork area */
  .panel-artwork {
    position: absolute;
    left: 0;
    top: 0;
    width: 396px;
    height: 848px;
    background:
      radial-gradient(ellipse 240px 360px at 260px 300px, var(--xray-light) 0%, rgba(233,244,255,0.85) 40%, rgba(63,147,234,0) 80%),
      linear-gradient(160deg, var(--xray-mid) 0%, var(--xray-deep) 100%);
  }
  .intro-statement {
    position: absolute;
    right: 40px;
    top: 214px;
    width: 260px;
    margin: 0;
    text-align: right;
    font-size: 19px;
    line-height: 29.3px;
    font-weight: 700;
    color: var(--brand-blue);
  }

  /* Middle panel: brands, locations and contact */
  .panel-info {
    position: absolute;
    left: 396px;
    top: 0;
    width: 400px;
    height: 848px;
  }
  .brand-list {
    position: absolute;
    left: 40px;
    top: 70px;
    width: 320px;
    margin: 0;
    padding: 0;
    list-style: none;
  }
  .brand-list-heading {
    position: absolute;
    left: 41px;
    top: 40px;
    margin: 0;
    font-size: 14px;
    font-weight: 700;
    letter-spacing: 0.2px;
    color: var(--ink);
  }
  .brand {
    padding: 7px 0 7px 0;
    border-bottom: 1px solid var(--rule);
  }
  .brand-name {
    display: block;
    font-size: 14px;
    line-height: 17px;
    font-weight: 700;
    color: var(--brand-blue);
  }
  .brand-service,
  .brand-web {
    display: block;
    font-size: 11px;
    line-height: 14px;
    color: var(--ink-soft);
  }
  .brand-web { color: var(--ink-muted); }

  .wordmark-small {
    position: absolute;
    left: 40px;
    top: 488px;
    margin: 0;
    font-size: 21px;
    line-height: 22px;
    font-weight: 700;
    letter-spacing: -0.5px;
    color: var(--brand-blue);
  }
  .section-heading {
    position: absolute;
    left: 41px;
    margin: 0;
    font-size: 14px;
    font-weight: 700;
    letter-spacing: 0.2px;
    color: var(--ink);
  }
  .locations-heading { top: 544px; }
  .contact-heading { top: 748px; }
  .location {
    position: absolute;
    margin: 0;
    font-size: 11px;
    line-height: 14px;
    font-style: normal;
    color: var(--ink-soft);
  }
  .location strong {
    display: block;
    color: var(--ink);
  }
  .col-a { left: 41px; }
  .col-b { left: 204px; }
  .row-1 { top: 566px; }
  .row-2 { top: 632px; }
  .row-3 { top: 688px; }
  .contact-list {
    position: absolute;
    left: 41px;
    top: 768px;
    margin: 0;
    display: grid;
    grid-template-columns: 52px auto;
    row-gap: 1px;
    font-size: 11px;
    line-height: 14px;
    color: var(--ink-soft);
  }
  .contact-list dt {
    font-weight: 700;
    color: var(--ink);
  }
  .contact-list dd { margin: 0; }

  /* Right panel: cover */
  .panel-cover {
    position: absolute;
    left: 796px;
    top: 0;
    width: 404px;
    height: 848px;
  }
  .wordmark-large {
    position: absolute;
    left: 40px;
    top: 108px;
    margin: 0;
    font-size: 54px;
    line-height: 48px;
    font-weight: 700;
    letter-spacing: -1.5px;
    color: var(--brand-blue);
  }
  .tagline {
    position: absolute;
    left: 41px;
    top: 218px;
    margin: 0;
    font-size: 20px;
    font-weight: 700;
    letter-spacing: 0.3px;
    color: var(--ink-soft);
  }
  .cover-photo {
    position: absolute;
    left: 44px;
    top: 286px;
    width: 300px;
    height: 562px;
    border-radius: 60px 60px 0 0;
    background:
      linear-gradient(90deg, rgba(255,255,255,0.9) 0%, rgba(255,255,255,0) 18%, rgba(255,255,255,0) 82%, rgba(255,255,255,0.9) 100%),
      linear-gradient(180deg, var(--skin-light) 0%, var(--skin-mid) 100%);
  }
</style>
</head>
<body>
<main class="brochure">

  <section class="panel-artwork" role="img" aria-label="Blue X-ray style illustration of a foot and ankle skeleton">
    <p class="intro-statement">Our specialist<br>foot health team<br>delivers the most<br>comprehensive<br>treatment solutions<br>in New Zealand<br>for fungal nail,<br>ingrown toenail,<br>cosmetic or general<br>nail conditions.</p>
  </section>

  <section class="panel-info">
    <h2 class="brand-list-heading">OUR BRANDS</h2>
    <ul class="brand-list">
      <li class="brand">
        <span class="brand-name">Brightmoor Solutions</span>
        <span class="brand-service">Fungal nail assessment and laser treatment</span>
        <span class="brand-web">www.brightmoorsolutions.example.nz</span>
      </li>
      <li class="brand">
        <span class="brand-name">Kestrelbay Solutions</span>
        <span class="brand-service">Ingrown toenail care and minor nail surgery</span>
      </li>
      <li class="brand">
        <span class="brand-name">Varden Solutions</span>
        <span class="brand-service">Heel pain diagnosis, orthotics and shockwave</span>
      </li>
      <li class="brand">
        <span class="brand-name">Tolverstone Rehabilitation</span>
        <span class="brand-service">Foot and ankle physiotherapy and injury rehab</span>
      </li>
      <li class="brand">
        <span class="brand-name">Ashgrove Solutions</span>
        <span class="brand-service">Cosmetic nail restoration and reconstruction</span>
      </li>
      <li class="brand">
        <span class="brand-name">Merriwether Solutions</span>
        <span class="brand-service">General podiatry, corns, calluses and skin care</span>
      </li>
    </ul>

    <p class="wordmark-small">Stridewell<br>Clinic</p>

    <h2 class="section-heading locations-heading">LOCATIONS</h2>

    <address class="location col-a row-1"><strong>Hamilton</strong>Suite 4/210<br>Larchmont Street<br>Hamilton Central</address>
    <address class="location col-b row-1"><strong>Auckland City</strong>Fenwick Lane Clinic<br>12 Fenwick Lane<br>Newmarket</address>
    <address class="location col-a row-2"><strong>Tauranga</strong>48 Harbourview Road<br>Otumoetai</address>
    <address class="location col-b row-2"><strong>North Shore</strong>207 Tamsin Road<br>Mildford</address>
    <address class="location col-a row-3"><strong>Rotorua</strong>1530 Kowhai Street<br>Rotorua</address>

    <h2 class="section-heading contact-heading">CONTACT US</h2>
    <dl class="contact-list">
      <dt>Phone</dt><dd>(07) 555 0142</dd>
      <dt>Web</dt><dd>www.stridewellclinic.example.nz</dd>
      <dt>Email</dt><dd>reception@stridewellclinic.example.nz</dd>
    </dl>
  </section>

  <section class="panel-cover">
    <h1 class="wordmark-large">Stridewell<br>Clinic</h1>
    <p class="tagline">Your Experts in Foot Health</p>
    <div class="cover-photo" role="img" aria-label="Photograph of two bare feet with toes raised, against a white background"></div>
  </section>

</main>
</body>
</html>
```